Larvik Consulting

Hi,
I have my own network consulting business (just me)
and need to get a logo and business card design together,

Based in New Zealand,

Tobias Wrenfield
Unified Communications and Network Architect

/design engineer,
and would like this to be the basis for personal branding and company identity

Industry/Entity Type

Business

Requirements
Nice to have
• I have the basis for a optional logo - needs color -

```html
<!DOCTYPE html>
<html lang="en">
<head>
<meta charset="utf-8">
<title>Larvik Consulting – Business Card</title>
<link rel="stylesheet" href="https://fonts.googleapis.com/css2?family=Exo+2:wght@600;700&family=Open+Sans:wght@400;700&display=swap">
<style>
  :root {
    --backdrop: #9b9ca0;
    --brand-blue: #1b4fa0;
    --brand-blue-bright: #1a64b8;
    --card-light: #f6f7f8;
    --card-mid: #dfe1e4;
    --card-shade: #c9ccd0;
    --ink: #1c1c1c;
    --white: #ffffff;
  }
  * { box-sizing: border-box; margin: 0; padding: 0; }
  html, body { width: 1200px; height: 900px; overflow: hidden; }
  body { background: var(--backdrop); position: relative; font-family: "Open Sans", sans-serif; }

  .card {
    position: absolute; top: 279px; width: 524px; height: 327px;
    border-radius: 14px; overflow: hidden;
    background: linear-gradient(180deg, var(--card-light) 0%, var(--card-mid) 55%, var(--card-light) 100%);
  }
  .card--front { left: 50px; }
  .card--back { left: 627px; }
  .card__swoosh { position: absolute; inset: 0; width: 100%; height: 100%; }

  .brand-mark { position: absolute; display: flex; align-items: center; gap: 10px; }
  .brand-mark__dot { border-radius: 50%; background: radial-gradient(circle at 35% 30%, var(--brand-blue-bright), var(--brand-blue)); flex: none; }
  .brand-mark__name { font-family: "Exo 2", sans-serif; font-weight: 700; color: var(--brand-blue); line-height: 1.15; }

  .card--front .brand-mark { left: 24px; top: 124px; }
  .card--front .brand-mark__dot { width: 64px; height: 64px; }
  .card--front .brand-mark__name { font-size: 21px; }

  .tagline-band {
    position: absolute; left: 212px; top: 131px; width: 312px; height: 58px;
    background: linear-gradient(180deg, var(--brand-blue-bright), var(--brand-blue));
    color: var(--white); font-family: "Exo 2", sans-serif; font-weight: 600;
    font-size: 19.5px; line-height: 23px; padding: 6px 0 0 33px;
  }

  .card--back .brand-mark { left: 40px; top: 26px; flex-direction: column; align-items: flex-start; gap: 8px; }
  .card--back .brand-mark__dot { width: 52px; height: 52px; margin-left: 8px; }
  .card--back .brand-mark__name { font-size: 15px; }

  .tagline { position: absolute; left: 174px; top: 48px; font-family: "Exo 2", sans-serif; font-weight: 600; font-size: 23.5px; line-height: 28px; color: var(--brand-blue); }

  .person-name { position: absolute; left: 92px; top: 204px; font-family: "Open Sans", sans-serif; font-weight: 700; font-size: 20px; color: var(--brand-blue); }

  .contact { position: absolute; left: 69px; top: 259px; list-style: none; }
  .contact__item { display: flex; align-items: center; gap: 10px; font-size: 14.5px; color: var(--ink); height: 27px; }
  .contact__icon { width: 17px; height: 12px; flex: none; }
</style>
</head>
<body>

<section class="card card--front" aria-label="Card front">
  <svg class="card__swoosh" viewBox="0 0 524 327" aria-hidden="true">
    <path d="M0 20 C120 -10 300 60 524 0 L524 0 L0 0 Z" fill="#ffffff" opacity="0.7"/>
    <path d="M20 40 C200 260 420 140 524 120" fill="none" stroke="#ffffff" stroke-width="14" opacity="0.5"/>
    <path d="M0 327 C160 240 340 205 524 215 L524 327 Z" fill="#ffffff" opacity="0.85"/>
    <path d="M30 327 C200 250 360 222 524 226" fill="none" stroke="#c4c7cb" stroke-width="3" opacity="0.8"/>
  </svg>
  <div class="brand-mark">
    <span class="brand-mark__dot"></span>
    <span class="brand-mark__name">Larvik<br>Consulting</span>
  </div>
  <div class="tagline-band">Unified Communications<br>and Network Architect</div>
</section>

<section class="card card--back" aria-label="Card back">
  <svg class="card__swoosh" viewBox="0 0 524 327" aria-hidden="true">
    <path d="M0 180 C180 120 360 150 524 110 L524 0 L0 0 Z" fill="#ffffff" opacity="0.55"/>
    <path d="M0 212 C180 200 360 210 524 250" fill="none" stroke="#ffffff" stroke-width="10" opacity="0.9"/>
    <path d="M0 327 C200 300 380 300 524 327 Z" fill="#ffffff" opacity="0.8"/>
  </svg>
  <div class="brand-mark">
    <span class="brand-mark__dot"></span>
    <span class="brand-mark__name">Larvik<br>Consulting</span>
  </div>
  <p class="tagline">Unified Communications<br>and Network Architect</p>
  <h1 class="person-name">Tobias Wrenfield</h1>
  <ul class="contact">
    <li class="contact__item">
      <svg class="contact__icon" viewBox="0 0 17 12" aria-hidden="true">
        <path d="M1 4 C1 1 16 1 16 4 L13 5 L12 3 L5 3 L4 5 Z" fill="#1b4fa0"/>
        <rect x="3" y="6" width="11" height="6" rx="1.5" fill="#1b4fa0"/>
        <circle cx="8.5" cy="9" r="1.6" fill="#fff"/>
      </svg>
      (+64) 555 010 247
    </li>
    <li class="contact__item">
      <svg class="contact__icon" viewBox="0 0 17 12" aria-hidden="true">
        <rect x="0.5" y="0.5" width="16" height="11" rx="1.5" fill="#1b4fa0"/>
        <circle cx="5" cy="5" r="1.8" fill="#fff"/>
        <rect x="2.5" y="7.5" width="5" height="2" fill="#fff"/>
        <rect x="9" y="3" width="6" height="1.3" fill="#fff"/>
        <rect x="9" y="6" width="6" height="1.3" fill="#fff"/>
      </svg>
      Level 12, 48 Harbour Lane, Northbridge, NSW, 2063
    </li>
  </ul>
</section>

</body>
</html>
```